Stationery Set for new venture capital firm

We need a new set of stationery including letterhead, business cards, envelopes, with compliment slips for our new startup venture capital firm known as Halvora.
We make alternative investments globally and hope to have a worldwide network of offices later.

The stationery should be elegant and not too fussy with the use of too many colors.

Venture Capital

```html
<!DOCTYPE html>
<html lang="en">
<head>
<meta charset="utf-8">
<title>Halvora Stationery Set</title>
<link rel="stylesheet" href="https://fonts.googleapis.com/css2?family=Varela+Round&family=Tinos&display=swap">
<style>
:root{
  --stage:#6e4d35;
  --paper:#ffffff;
  --brand-blue:#1e9bd7;
  --brand-grey:#8a8a8a;
  --rule-grey:#9a9a9a;
  --ghost:#e6f1f8;
  --ink:#3a3a3a;
  --label:#ffffff;
  --env-grey:#8f8f8f;
  --env-shade:#e9e9e9;
}
*{box-sizing:border-box;margin:0;padding:0}
html,body{width:1200px;height:517px;overflow:hidden}
body{background:var(--stage);position:relative;font-family:"Tinos",serif;color:var(--ink)}
.sheet{position:absolute;background:var(--paper);overflow:hidden}
.brand{position:absolute;display:flex;flex-direction:column;align-items:center;gap:4px}
.brand-dot{border-radius:50%;background:var(--brand-blue)}
.brand-name{font-family:"Varela Round",sans-serif;color:var(--brand-grey);line-height:1}
.ghost-mark{position:absolute;border-radius:50%;background:var(--ghost)}
.footer-rule{position:absolute;left:0;right:0;height:3px;background:var(--rule-grey)}
.footer-band{position:absolute;left:0;right:0;background:var(--brand-blue);color:#fff;font-size:6px;text-align:center}
.contact-row{display:flex;justify-content:center;gap:12px;padding-top:5px}
.contact-row span::before{content:"";display:inline-block;width:4px;height:4px;border-radius:50%;background:#fff;margin-right:3px;vertical-align:middle}
.label{position:absolute;top:474px;font-size:25px;color:var(--label);width:200px;text-align:center}

/* letterhead */
.letterhead{left:22px;top:18px;width:336px;height:437px}
/* fax */
.fax{left:416px;top:20px;width:337px;height:438px}
.fax-address{position:absolute;left:253px;top:28px;border-left:1px solid var(--ink);padding-left:4px;font-size:6px;line-height:9px}
.fax-title{position:absolute;left:17px;top:104px;font-size:22px;letter-spacing:1px}
.fax-field{position:absolute;font-size:6px;border-bottom:1px solid var(--ink);padding-bottom:1px;height:9px}
.fax-checks{position:absolute;left:17px;top:227px;display:flex;gap:13px;font-size:6px}
.fax-checks span::before{content:"";display:inline-block;width:7px;height:7px;border:1px solid var(--ink);margin-right:6px;vertical-align:middle}

/* envelopes */
.envelope-back{position:absolute}
.envelope-front{left:769px;top:182px;width:376px;height:168px;box-shadow:0 2px 4px rgba(0,0,0,.3)}
.envelope-front .footer-band{text-align:left;display:flex;justify-content:space-between;padding:3px 10px 0 16px}

/* business cards */
.card{position:absolute;top:380px;width:138px;height:77px}
.card-front{left:790px;background:var(--paper)}
.card-divider{position:absolute;left:74px;top:10px;width:1px;height:46px;background:var(--ink)}
.card-details{position:absolute;left:83px;top:13px;font-size:5px;line-height:7px}
.card-details .card-name{font-size:6px}
.card-front .footer-band{top:70px;height:7px;font-size:3px;padding-top:2px}
.card-back{left:937px;background:var(--brand-blue);display:flex;align-items:center;justify-content:center}
.card-back .brand-name{color:#fff;font-size:22px}
</style>
</head>
<body>

<!-- Letterhead -->
<section class="sheet letterhead">
  <div class="brand" style="left:134px;top:6px">
    <div class="brand-dot" style="width:26px;height:26px"></div>
    <div class="brand-name" style="font-size:19px">Halvora</div>
  </div>
  <div class="ghost-mark" style="left:40px;top:150px;width:250px;height:250px"></div>
  <div class="footer-rule" style="top:406px"></div>
  <div class="footer-band" style="top:410px;height:27px">
    <div class="contact-row"><span>123-456-7890</span><span>123-456-7856</span><span>hello@halvora.com</span><span>www.halvora.com</span></div>
    <div>Street Name, City Name State Zipcode</div>
  </div>
</section>
<div class="label" style="left:90px">Option-1</div>

<!-- Fax -->
<section class="sheet fax">
  <div class="brand" style="left:17px;top:12px">
    <div class="brand-dot" style="width:26px;height:26px"></div>
    <div class="brand-name" style="font-size:19px">Halvora</div>
  </div>
  <div class="fax-address">Street Name, City Name<br>State Zipcode</div>
  <h1 class="fax-title" style="font-weight:400">FAX</h1>
  <div class="fax-field" style="left:17px;top:143px;width:157px">To :</div>
  <div class="fax-field" style="left:189px;top:143px;width:116px">From :</div>
  <div class="fax-field" style="left:17px;top:161px;width:157px">Fax :</div>
  <div class="fax-field" style="left:189px;top:161px;width:116px">Pages :</div>
  <div class="fax-field" style="left:17px;top:178px;width:157px">Phone :</div>
  <div class="fax-field" style="left:189px;top:178px;width:116px">Date :</div>
  <div class="fax-field" style="left:17px;top:196px;width:157px">Re :</div>
  <div class="fax-field" style="left:189px;top:196px;width:116px">CC :</div>
  <div class="fax-checks"><span>Urgent</span><span>For Review</span><span>Please Comment</span><span>Please Reply</span><span>Please Recycle</span></div>
  <div class="ghost-mark" style="left:103px;top:292px;width:102px;height:102px"></div>
  <div class="footer-rule" style="top:410px"></div>
  <div class="footer-band" style="top:415px;height:23px">
    <div class="contact-row" style="padding-top:7px"><span>123-456-7890</span><span>123-456-7856</span><span>hello@halvora.com</span><span>www.halvora.com</span></div>
  </div>
</section>
<div class="label" style="left:497px">Option-2</div>

<!-- Envelopes (back views) -->
<svg class="envelope-back" style="left:795px;top:0" width="376" height="270" viewBox="0 0 376 270">
  <rect x="13" y="0" width="337" height="255" fill="#ffffff"/>
  <path d="M13 0 H350 V18 Q290 62 205 72 Q180 75 155 72 Q70 62 13 18 Z" fill="var(--brand-blue)"/>
  <circle cx="182" cy="44" r="20" fill="#ffffff" opacity=".2"/>
  <rect x="0" y="97" width="375" height="168" fill="var(--env-shade)"/>
  <path d="M0 97 H375 V118 Q300 148 205 153 Q187 154 170 153 Q75 148 0 118 Z" fill="var(--env-grey)"/>
  <circle cx="187" cy="125" r="20" fill="#ffffff" opacity=".2"/>
</svg>

<!-- Envelope (front) -->
<section class="sheet envelope-front">
  <div class="brand" style="left:17px;top:6px">
    <div class="brand-dot" style="width:28px;height:28px"></div>
    <div class="brand-name" style="font-size:18px">Halvora</div>
  </div>
  <div class="ghost-mark" style="left:250px;top:38px;width:110px;height:110px"></div>
  <div class="footer-rule" style="top:150px"></div>
  <div class="footer-band" style="top:155px;height:13px"><span>Street Name, City Name State Zipcode</span><span>www.halvora.com</span></div>
</section>

<!-- Business cards -->
<section class="card card-front">
  <div class="brand" style="left:10px;top:14px">
    <div class="brand-dot" style="width:22px;height:22px"></div>
    <div class="brand-name" style="font-size:13px">Halvora</div>
  </div>
  <div class="card-divider"></div>
  <div class="card-details">
    <div class="card-name">Your Name</div>
    <div>Title</div>
    <div style="margin-top:4px">123-456-7890</div>
    <div>123-456-7856</div>
    <div>hello@halvora.com</div>
    <div>www.halvora.com</div>
  </div>
  <div class="footer-band">Street Name, City Name State Zipcode</div>
</section>
<section class="card card-back">
  <div class="brand-name">Halvora</div>
</section>

</body>
</html>
```